Health Coaching Flyer for New Clients

I need a two-sided flyer (3.5" x 8.5" preferred or 5" x 7") to distribute to potential coaching clients. My business name is Talvery Health & Wellness Coaching. My business is focused on helping people with habit changes that contribute to their overall well-being. I would like the design colors to be gender neutral. I would like a small photo of myself near the "my name is Joan" statement. Please feel free to change the logo color to match the design.

Target Market(s)

Adults of all ages.

Font styles to use
Serif

Requirements
Must have
• Emphasize my opening question (found in health coaching brochure - attached).
• Small picture of myself near "my name is Joan" statement.
Should not have
• No light of pastel colors.

```html
<!DOCTYPE html>
<html lang="en">
<head>
<meta charset="utf-8">
<title>Talvery Health &amp; Wellness Coaching – Flyer</title>
<link rel="stylesheet" href="https://fonts.googleapis.com/css2?family=Open+Sans:ital,wght@0,400;0,600;0,700;0,800;1,700&display=swap">
<style>
  :root{
    --page:#e6e5e1;
    --green:#6cae2f;
    --green-dark:#4f8f1e;
    --lime:#a9d24b;
    --orange:#f2a516;
    --heading-yellow:#fbe46a;
    --text-white:#ffffff;
    --contact-green:#5f9a2a;
    --name-grey:#9a9a9a;
  }
  *{box-sizing:border-box;margin:0;padding:0}
  html,body{width:1127px;height:1200px;overflow:hidden}
  body{background:var(--page);font-family:"Open Sans",Arial,sans-serif;position:relative}

  .flyer{
    position:absolute;top:55px;width:500px;height:1090px;overflow:hidden;
    background:linear-gradient(180deg,var(--green) 0%,var(--green-dark) 100%);
    box-shadow:0 4px 14px rgba(0,0,0,.25);
    color:var(--text-white);
  }
  .flyer--front{left:40px}
  .flyer--back{left:587px}
  .flyer__art{position:absolute;inset:0;width:500px;height:1090px}

  .brand{position:absolute;top:498px;left:0;width:500px;text-align:center;color:var(--text-white);font-weight:700}
  .brand__name{font-size:58px;letter-spacing:5px;line-height:1}
  .brand__tag{font-size:13px;letter-spacing:1.5px;margin-top:6px}

  .headline{position:absolute;top:612px;left:30px;width:440px;text-align:center;font-size:20px;font-weight:800;line-height:1.32;text-transform:uppercase}
  .rule{position:absolute;left:40px;width:420px;height:1px;background:rgba(255,255,255,.55)}
  .rule--front{top:686px}
  .intro{position:absolute;top:700px;left:40px;width:420px;font-size:14.2px;line-height:1.36;text-align:justify}
  .intro strong{display:block;font-weight:700}

  .signoff{position:absolute;top:898px;left:40px;width:240px;font-size:14px;font-style:italic;font-weight:700;line-height:1.3}
  .contact{position:absolute;left:38px;font-size:15px;font-weight:700;color:var(--contact-green);display:flex;align-items:center;gap:9px}
  .contact--phone{top:1030px}
  .contact--mail{top:1058px}
  .contact__icon{width:20px;height:20px}
  .coach-name{position:absolute;top:1044px;left:325px;width:140px;text-align:center;font-size:16px;font-weight:600;color:var(--name-grey)}

  .section-title{position:absolute;top:352px;left:40px;font-size:19px;font-weight:800;color:var(--heading-yellow)}
  .rule--back{top:386px;width:160px;background:var(--heading-yellow)}
  .benefits{position:absolute;top:402px;left:40px;width:425px;list-style:none;font-size:14px;line-height:1.32}
  .benefits li{padding-left:14px;position:relative;margin-bottom:12px}
  .benefits li::before{content:"•";position:absolute;left:0}
  .invite{position:absolute;top:688px;left:40px;width:425px;font-size:14px;line-height:1.36}
  .offer{position:absolute;top:772px;left:40px;width:420px;height:76px;border-radius:7px;background:var(--orange);
         display:flex;align-items:center;justify-content:center;text-align:center;font-size:14px;font-weight:700;line-height:1.3;padding:0 24px}
</style>
</head>
<body>

<section class="flyer flyer--front">
  <svg class="flyer__art" viewBox="0 0 500 1090">
    <defs>
      <linearGradient id="front-photo-tone" x1="0" y1="0" x2="1" y2="1">
        <stop offset="0" stop-color="#f1efe9"/>
        <stop offset=".55" stop-color="#c9d6c0"/>
        <stop offset="1" stop-color="#8fae6a"/>
      </linearGradient>
      <linearGradient id="front-footer" x1="0" y1="0" x2="0" y2="1">
        <stop offset="0" stop-color="#ffffff"/>
        <stop offset="1" stop-color="#eef3e2"/>
      </linearGradient>
      <linearGradient id="front-portrait" x1="0" y1="0" x2="0" y2="1">
        <stop offset="0" stop-color="#8a5a44"/>
        <stop offset="1" stop-color="#d9a88c"/>
      </linearGradient>
    </defs>
    <path role="img" aria-label="Photo of a smiling woman eating a fresh salad beside jars of green and red juice"
          d="M0 0 H500 V415 Q300 500 0 450 Z" fill="url(#front-photo-tone)"/>
    <path d="M0 450 Q300 500 500 415 L500 440 Q300 520 0 472 Z" fill="var(--orange)"/>
    <path d="M0 470 Q300 515 500 438" fill="none" stroke="var(--lime)" stroke-width="3"/>
    <path d="M0 1018 Q260 975 500 1000 V1090 H0 Z" fill="url(#front-footer)"/>
    <path d="M0 1016 Q260 973 500 998" fill="none" stroke="var(--orange)" stroke-width="5"/>
    <circle cx="395" cy="950" r="72" fill="#ffffff"/>
    <circle role="img" aria-label="Small portrait photo of coach Joan Talvery" cx="395" cy="950" r="63" fill="url(#front-portrait)"/>
  </svg>

  <div class="brand">
    <div class="brand__name">TALVERY</div>
    <div class="brand__tag">HEALTH &amp; WELLNESS COACHING</div>
  </div>

  <h1 class="headline">Need support in making real, lasting lifestyle and behavior changes?</h1>
  <div class="rule rule--front"></div>

  <p class="intro"><strong>My name is Joan.</strong>I am studying to become an THRIVE - Certified Functional Health Coach. My training involves many science-based practices that improve both our health and how we grow and change as humans. I now have the opportunity to turn that knowledge into practice by coaching actual clients interested in improving their own health and wellbeing.</p>

  <p class="signoff">Please contact me.<br>I'm ready to support you as you work to improve your health.<br>- Joan Talvery</p>

  <div class="contact contact--phone">
    <svg class="contact__icon" viewBox="0 0 20 20"><circle cx="10" cy="10" r="10" fill="var(--orange)"/><path d="M6.5 5.2l2 .2.7 2.3-1.2 1a6 6 0 0 0 3.3 3.3l1-1.2 2.3.7.2 2c-.2.6-1 1-1.7.9A8.5 8.5 0 0 1 5.6 6.9c-.1-.7.3-1.5.9-1.7z" fill="#fff"/></svg>
    520-555-0147
  </div>
  <div class="contact contact--mail">
    <svg class="contact__icon" viewBox="0 0 20 20"><circle cx="10" cy="10" r="10" fill="var(--orange)"/><rect x="5" y="6.5" width="10" height="7" rx="1" fill="#fff"/><path d="M5.3 7l4.7 3.6L14.7 7" fill="none" stroke="var(--orange)" stroke-width="1.1"/></svg>
    talveryhwc@mailhaven.com
  </div>
  <div class="coach-name">Joan Talvery</div>
</section>

<section class="flyer flyer--back">
  <svg class="flyer__art" viewBox="0 0 500 1090">
    <defs>
      <linearGradient id="back-photo-tone" x1="0" y1="0" x2="0" y2="1">
        <stop offset="0" stop-color="#dfe9f0"/>
        <stop offset=".4" stop-color="#9fb7a8"/>
        <stop offset=".6" stop-color="#5f8a45"/>
        <stop offset="1" stop-color="#a9c46a"/>
      </linearGradient>
      <linearGradient id="back-footer" x1="0" y1="0" x2="0" y2="1">
        <stop offset="0" stop-color="#ffffff"/>
        <stop offset="1" stop-color="#eef3e2"/>
      </linearGradient>
      <linearGradient id="back-portrait" x1="0" y1="0" x2="0" y2="1">
        <stop offset="0" stop-color="#8a5a44"/>
        <stop offset="1" stop-color="#d9a88c"/>
      </linearGradient>
    </defs>
    <path role="img" aria-label="Photo of a woman with arms outstretched in a green meadow below mountains"
          d="M0 0 H500 V275 Q260 350 0 298 Z" fill="url(#back-photo-tone)"/>
    <path d="M0 298 Q260 350 500 275 L500 296 Q260 372 0 316 Z" fill="var(--orange)"/>
    <circle cx="505" cy="-5" r="70" fill="var(--lime)"/>
    <path d="M0 1018 Q260 975 500 1000 V1090 H0 Z" fill="url(#back-footer)"/>
    <path d="M0 1016 Q260 973 500 998" fill="none" stroke="var(--orange)" stroke-width="5"/>
    <circle cx="395" cy="950" r="72" fill="#ffffff"/>
    <circle role="img" aria-label="Small portrait photo of coach Joan Talvery" cx="395" cy="950" r="63" fill="url(#back-portrait)"/>
  </svg>

  <h2 class="section-title">FUNCTIONAL HEALTH COACHES…</h2>
  <div class="rule rule--back"></div>

  <ul class="benefits">
    <li>Leverage your strengths rather than focus on your weaknesses</li>
    <li>Support you in finding your own strategies and motivation for change</li>
    <li>Provide a judgment-free zone and support your autonomy</li>
    <li>Use an experimental mindset to find and develop sustainable habits</li>
    <li>Act as your accountability partner as you reach your unique health goals; whether they be improving sleep, diet, fitness, social connection, or reducing stress.</li>
  </ul>

  <p class="invite">I would like to invite you to participate with me as a client as I continue to hone my coaching skills. We can develop a plan and schedule that aligns with your goals.</p>

  <div class="offer">As a way to give back to my community, I am offering new clients six free coaching sessions. This is a limited time offer.</div>

  <p class="signoff">Please contact me.<br>I'm ready to support you as you work to improve your health.<br>- Joan Talvery</p>

  <div class="contact contact--phone">
    <svg class="contact__icon" viewBox="0 0 20 20"><circle cx="10" cy="10" r="10" fill="var(--orange)"/><path d="M6.5 5.2l2 .2.7 2.3-1.2 1a6 6 0 0 0 3.3 3.3l1-1.2 2.3.7.2 2c-.2.6-1 1-1.7.9A8.5 8.5 0 0 1 5.6 6.9c-.1-.7.3-1.5.9-1.7z" fill="#fff"/></svg>
    520-555-0147
  </div>
  <div class="contact contact--mail">
    <svg class="contact__icon" viewBox="0 0 20 20"><circle cx="10" cy="10" r="10" fill="var(--orange)"/><rect x="5" y="6.5" width="10" height="7" rx="1" fill="#fff"/><path d="M5.3 7l4.7 3.6L14.7 7" fill="none" stroke="var(--orange)" stroke-width="1.1"/></svg>
    talveryhwc@mailhaven.com
  </div>
  <div class="coach-name">Joan Talvery</div>
</section>

</body>
</html>
```